Website Re-Design Project

We have popular voucher code website and we would like to make re-design for whole website. Including following pages: Home page, store page, listing page, article page and blog page.

Our website is: www.tarvelumio.com. Its non english language but you will get the point.

Design should be clean, stylish and highly conversion. At the moment there is too much thing in homepage. Example the carusel should be removed. We want keep our main colours green and orange.

Please look our home page mockup from files. That is only one option and we are open to see different choises for the layout.

Inspirations :
http://www.plimbertons.co.uk/
http://www.grovelindamerhof.nl/
http://www.truffelwicketbramblers.co.uk/

Target Market(s)

People who are looking vouchers and coupon codes for the online shops.

Industry/Entity Type

Store

Requirements
Should not have
• Any carusels

```html
<!DOCTYPE html>
<html lang="en">
<head>
<meta charset="utf-8">
<title>Tarvelumio.com – Voucher Codes</title>
<link rel="stylesheet" href="https://fonts.googleapis.com/css2?family=Shanti&family=Ubuntu:wght@400;500;700&display=swap">
<style>
:root{
  --bg:#1c1c1c;
  --panel-top:#2a2a2a;
  --panel-bottom:#181818;
  --panel-border:#3a3a3a;
  --green:#7cbf12;
  --green-light:#9bd62a;
  --green-dark:#5c9a08;
  --orange:#ff7a00;
  --orange-light:#ffa23a;
  --text:#ffffff;
  --text-soft:#ececec;
  --muted:#8a8a8a;
  --row-line:#333333;
  --friend:#3b8ee8;
  --tile-pink:#ec0c8c;
  --tile-grey:#777777;
  --tile-red:#c8282a;
  --tile-blue:#2b79c8;
  --tile-teal:#27c56c;
  --tile-purple:#5f2dc8;
}
*{box-sizing:border-box;margin:0;padding:0}
html,body{width:786px;height:1200px;overflow:hidden;background:var(--bg)}
body{font-family:"Ubuntu",sans-serif;color:var(--text);position:relative}
.page{position:relative;width:786px;height:1200px}
.abs{position:absolute}

.site-name{left:27px;top:48px;font-family:"Shanti",sans-serif;font-size:27px;color:var(--green-light);letter-spacing:.3px}

.main-nav{left:364px;top:38px;width:401px;height:47px;display:flex;border-radius:4px;overflow:hidden;
  background:linear-gradient(var(--green-light),var(--green) 50%,var(--green-dark));border:1px solid #8fd12a}
.main-nav a{flex:auto;display:flex;align-items:center;justify-content:center;color:var(--text);text-decoration:none;
  font-family:"Ubuntu",sans-serif;font-weight:500;font-size:13px;border-right:1px solid rgba(0,0,0,.15);text-shadow:0 1px 1px rgba(0,0,0,.3)}
.main-nav a:last-child{border-right:0}
.main-nav a.current{color:#e8f96a}

.hero-count{left:0;width:786px;top:200px;text-align:center;font-family:"Shanti",sans-serif;font-size:22px;color:var(--muted);letter-spacing:.4px}
.hero-title{left:0;width:786px;top:232px;text-align:center;font-family:"Shanti",sans-serif;font-weight:400;font-size:28px;color:var(--green);letter-spacing:.4px}

.search-field{left:209px;top:287px;width:269px;height:36px;background:#262626;border:1px solid #111;border-radius:2px;
  font-family:"Shanti",sans-serif;font-size:15px;color:#eee;padding:9px 0 0 9px}
.search-button{left:493px;top:289px;width:79px;height:33px;border-radius:2px;background:linear-gradient(var(--green-light),var(--green-dark));
  font-family:"Shanti",sans-serif;font-size:14px;display:flex;align-items:center;justify-content:center;box-shadow:0 2px 2px #000}

.store-tile{top:374px;width:57px;height:61px;border-radius:3px;display:flex;align-items:center;justify-content:center;
  font-family:"Ubuntu",sans-serif;font-weight:700;font-size:16px;color:#fff;border:1px solid rgba(255,255,255,.15)}

.list-box{top:499px;width:138px;height:229px;border:1px solid var(--panel-border);border-radius:3px;
  background:linear-gradient(var(--panel-top),var(--panel-bottom));overflow:hidden}
.list-box h2{height:31px;background:linear-gradient(var(--green-light),var(--green) 55%,var(--green-dark));
  font-family:"Ubuntu",sans-serif;font-weight:500;font-size:11px;text-align:center;line-height:31px}
.list-box ul{list-style:none;padding:4px 4px 0}
.list-box li{font-size:8.5px;font-weight:500;color:var(--text-soft);height:19.4px;line-height:19px;padding-left:2px;
  border-bottom:1px solid var(--row-line);white-space:nowrap;overflow:hidden}

.newsletter-bar{left:114px;top:745px;width:536px;height:32px;border-radius:3px;
  background:linear-gradient(var(--orange-light) 50%,var(--orange) 50%);font-family:"Ubuntu",sans-serif;font-weight:500;font-size:10.5px;padding:14px 0 0 14px}

.panel{border:1px solid var(--panel-border);border-radius:3px;background:linear-gradient(var(--panel-top),var(--panel-bottom))}
.featured{left:114px;top:790px;width:536px;height:166px}
.featured h3{font-family:"Ubuntu",sans-serif;font-weight:500;font-size:11px;position:absolute;left:10px;top:10px}
.featured-row{position:absolute;left:8px;width:520px;height:19.5px;border-bottom:1px solid var(--row-line);font-size:8px;font-weight:500;color:var(--text-soft)}
.featured-row span{position:absolute;top:6px;white-space:nowrap}

.welcome{left:114px;top:969px;width:273px;height:138px}
.welcome h3,.socials h3{font-family:"Ubuntu",sans-serif;font-weight:500;font-size:12px;text-align:center;margin-top:17px}
.accent-green{color:var(--green)}
.accent-blue{color:var(--friend)}
.welcome p{font-size:6.4px;font-weight:500;line-height:8.6px;padding:11px 11px 0 11px;color:var(--text-soft)}
.socials{left:400px;top:969px;width:249px;height:138px}
.socials p{font-size:8px;font-weight:500;color:var(--muted);text-align:center;margin-top:12px;line-height:12px;padding:0 20px}
</style>
</head>
<body>
<div class="page">
  <div class="abs site-name">Tarvelumio.com</div>
  <nav class="abs main-nav">
    <a class="current" href="#">Home</a><a href="#">Top20</a><a href="#">Latest</a><a href="#">Shops</a><a href="#">Categories</a>
  </nav>

  <p class="abs hero-count">Find 612 active vouchers today.</p>
  <h1 class="abs hero-title">Brightpenny Voucher Codes.</h1>

  <div class="abs search-field">Search a store..</div>
  <div class="abs search-button">Search</div>

  <div class="abs store-tile" style="left:146px;background:var(--tile-pink)">lumo</div>
  <div class="abs store-tile" style="left:228px;background:var(--tile-grey)">lumo</div>
  <div class="abs store-tile" style="left:310px;background:var(--tile-red)">lumo</div>
  <div class="abs store-tile" style="left:392px;background:var(--tile-blue)">lumo</div>
  <div class="abs store-tile" style="left:474px;background:var(--tile-teal)">lumo</div>
  <div class="abs store-tile" style="left:557px;background:var(--tile-purple)">lumo</div>

  <section class="abs list-box" style="left:116px">
    <h2>Top20</h2>
    <ul><li>Lumo – 20% off fashion</li><li>Kettlebrook – free delivery</li><li>Norvale Home – £10 off</li><li>Pinecrest Sports – 15% off</li><li>Ambly Books – 3 for 2</li></ul>
  </section>
  <section class="abs list-box" style="left:316px">
    <h2>Latest</h2>
    <ul><li>Velmora Beauty – 25% off</li><li>Tidewell Travel – £30 off</li><li>Quillfield Tech – 10% off</li><li>Harrowgate Toys – half price</li><li>Brisk Pet Shop – free gift</li></ul>
  </section>
  <section class="abs list-box" style="left:511px">
    <h2>Categories</h2>
    <ul><li>Fashion &amp; Clothing</li><li>Electronics</li><li>Home &amp; Garden</li><li>Travel &amp; Holidays</li><li>Health &amp; Beauty</li></ul>
  </section>

  <div class="abs newsletter-bar">Newsletter</div>

  <section class="abs panel featured">
    <h3>Featured Stories</h3>
    <div class="featured-row" style="top:32px"><span style="left:5px">How to stack discount codes</span><span style="left:233px">Best summer sale deals</span><span style="left:419px">Free delivery guide</span></div>
    <div class="featured-row" style="top:51.5px"><span style="left:5px">Saving tips for students</span><span style="left:233px">Top 10 fashion codes</span><span style="left:419px">Cashback explained</span></div>
    <div class="featured-row" style="top:71px"><span style="left:5px">Black Friday checklist</span><span style="left:233px">Cheaper holiday bookings</span><span style="left:419px">Tech deals this week</span></div>
    <div class="featured-row" style="top:90.5px"><span style="left:5px">Spotting expired vouchers</span><span style="left:233px">Family budget ideas</span><span style="left:419px">New shops added</span></div>
    <div class="featured-row" style="top:110px;height:22px"><span style="left:5px;top:9px">Gift ideas under £20</span><span style="left:233px;top:9px">Garden savings guide</span><span style="left:419px;top:9px">Reader favourites</span></div>
  </section>

  <section class="abs panel welcome">
    <h3>Welcome to <span class="accent-green">Tarvelumio.com</span></h3>
    <p>Tarvelumio.com gathers the newest voucher codes and discount offers from hundreds of online shops in one place. Every code is checked by our team each day so you can shop with confidence and save money on fashion, electronics, travel, home and much more. Search for your favourite store, copy the code and paste it at checkout. Join our newsletter to receive the best weekly deals straight to your inbox, and follow us to hear about flash sales first. Happy saving!</p>
  </section>

  <section class="abs panel socials">
    <h3><span class="accent-blue">Friendloop</span> Socials</h3>
    <p>Follow us for daily deals and flash sale alerts. 12,400 shoppers already do.</p>
  </section>
</div>
</body>
</html>
```